Airport Advertising Brochure

I need a flyer put together asap! Previous example included. Would like something clean and updated. New logo and updated company name. I would like this designed in Pages or Illustrator so I can update content when needed. Website: pagelantern.com

Target Market(s)

Authors. This page has some good content about what we do: https://www.pagelantern.com/terminalpromos/

Industry/Entity Type

Airport

Font styles to use
Serif
Sans Serif

Requirements
Must have
• Clean, modern design.

```html
<!DOCTYPE html>
<html lang="en">
<head>
<meta charset="utf-8">
<title>PageLantern — Airport Advertising</title>
<link href="https://fonts.googleapis.com/css2?family=Montserrat:wght@300;400;500&display=swap" rel="stylesheet">
<style>
  :root{
    --yellow:#fbdd14;
    --ink:#3a3a3c;
    --charcoal:#404043;
    --footer:#363638;
    --paper:#ffffff;
    --soft:#e4e4e4;
  }
  *{margin:0;padding:0;box-sizing:border-box}
  html,body{width:848px;height:1200px;overflow:hidden;background:var(--paper)}
  body{font-family:"Montserrat",Arial,sans-serif;color:var(--ink)}
  .flyer{position:relative;width:848px;height:1200px;overflow:hidden}
  .shapes{position:absolute;inset:0;width:848px;height:1200px}
  .brand{position:absolute;top:168px;left:0;width:848px;text-align:center;
    font-weight:400;font-size:30px;letter-spacing:-0.5px;color:var(--ink)}
  .value{position:absolute;top:229px;text-align:center;font-weight:300;
    font-size:21.5px;line-height:26.4px;color:var(--ink)}
  .value--left{left:70px;width:180px}
  .value--mid{left:344px;width:160px}
  .value--right{left:598px;width:174px}
  .intro{position:absolute;left:180px;width:488px;text-align:center;
    font-weight:300;font-size:15.2px;line-height:23.2px;color:var(--ink)}
  .intro strong{font-weight:500}
  .intro--one{top:416px}
  .intro--two{top:530px}
  .service{position:absolute;top:846px;text-align:center;color:var(--paper)}
  .service h2{font-weight:500;font-size:20.5px;line-height:26.4px;margin-bottom:14px}
  .service p{font-weight:300;font-size:15.2px;line-height:23.3px;color:var(--soft)}
  .service--launch{left:16px;width:248px}
  .service--launch h2{margin-bottom:11px}
  .service--airport{left:300px;width:248px}
  .service--speaker{left:584px;width:248px}
  .contact{position:absolute;top:1133px;left:0;width:848px;display:flex;
    align-items:center;color:var(--paper);font-size:13px;font-weight:300}
  .contact span{position:absolute;display:flex;align-items:center;gap:6px;white-space:nowrap}
  .contact svg{flex:none}
</style>
</head>
<body>
<main class="flyer">
  <svg class="shapes" viewBox="0 0 1060 1500" aria-hidden="false">
    <defs>
      <clipPath id="cornerLeft"><polygon points="0,0 240,0 0,240"/></clipPath>
      <clipPath id="cornerRight"><polygon points="820,0 1060,0 1060,240"/></clipPath>
      <marker id="tip" viewBox="0 0 10 10" refX="9" refY="5" markerWidth="7" markerHeight="7" orient="auto">
        <path d="M0,0 L10,5 L0,10" fill="none" stroke="#3a3a3c" stroke-width="1.6"/>
      </marker>
      <marker id="tipLight" viewBox="0 0 10 10" refX="9" refY="5" markerWidth="7" markerHeight="7" orient="auto">
        <path d="M0,0 L10,5 L0,10" fill="none" stroke="#2a2a2c" stroke-width="1.6"/>
      </marker>
      <linearGradient id="bulbTones" x1="0" y1="0" x2="1" y2="1">
        <stop offset="0" stop-color="#8d8f90"/><stop offset="1" stop-color="#3f4143"/>
      </linearGradient>
      <linearGradient id="shelfTones" x1="0" y1="0" x2="0" y2="1">
        <stop offset="0" stop-color="#7a4a2a"/><stop offset=".5" stop-color="#2f5f6a"/><stop offset="1" stop-color="#3a2a28"/>
      </linearGradient>
    </defs>

    <!-- corner stripes -->
    <g clip-path="url(#cornerLeft)" stroke="#fbdd14" stroke-width="26">
      <line x1="-20" y1="60" x2="60" y2="-20"/>
      <line x1="-20" y1="130" x2="130" y2="-20"/>
      <line x1="-20" y1="200" x2="200" y2="-20"/>
      <line x1="-20" y1="270" x2="270" y2="-20"/>
    </g>
    <g clip-path="url(#cornerRight)" stroke="#fbdd14" stroke-width="26">
      <line x1="1000" y1="-20" x2="1080" y2="60"/>
      <line x1="930" y1="-20" x2="1080" y2="130"/>
      <line x1="860" y1="-20" x2="1080" y2="200"/>
      <line x1="790" y1="-20" x2="1080" y2="270"/>
    </g>

    <!-- corner arrows -->
    <line x1="90" y1="210" x2="255" y2="35" stroke="#3a3a3c" stroke-width="2" marker-end="url(#tip)"/>
    <line x1="810" y1="35" x2="985" y2="215" stroke="#3a3a3c" stroke-width="2" marker-end="url(#tip)"/>

    <!-- brand square -->
    <rect x="496" y="74" width="68" height="68" fill="none" stroke="#fbdd14" stroke-width="2"/>

    <!-- guide lines -->
    <g stroke="#fbdd14" stroke-width="2.5" fill="none">
      <line x1="448" y1="276" x2="152" y2="572"/>
      <line x1="612" y1="276" x2="908" y2="572"/>
      <line x1="98" y1="772" x2="170" y2="842"/>
      <line x1="170" y1="842" x2="0" y2="1012"/>
      <line x1="962" y1="772" x2="890" y2="842"/>
      <line x1="890" y1="842" x2="1060" y2="1012"/>
      <polyline points="372,990 530,832 688,990"/>
    </g>
    <line x1="97" y1="451" x2="248" y2="451" stroke="#fbdd14" stroke-width="5"/>
    <line x1="812" y1="451" x2="964" y2="451" stroke="#fbdd14" stroke-width="5"/>

    <!-- centre arrow -->
    <line x1="455" y1="485" x2="605" y2="485" stroke="#3a3a3c" stroke-width="2" marker-end="url(#tip)"/>

    <!-- photo panels -->
    <polygon points="30,445 228,645 30,845 0,845 0,445" fill="url(#bulbTones)" role="img" aria-label="Photo of a light bulb lying on a chalkboard"/>
    <polygon points="1030,445 832,645 1030,845 1060,845 1060,445" fill="url(#shelfTones)" role="img" aria-label="Photo of colourful books on library shelves"/>
    <polygon points="175,667 203,695 175,723 147,695" fill="#fbdd14"/>
    <polygon points="908,673 950,715 908,757 866,715" fill="#fbdd14"/>

    <!-- dark service band -->
    <polygon points="0,1030 178,855 355,1030 530,855 707,1030 885,855 1060,1030 1060,1500 0,1500" fill="#404043"/>
    <rect x="0" y="1362" width="1060" height="138" fill="#363638"/>

    <!-- peak arrows -->
    <g stroke="#2a2a2c" stroke-width="2">
      <line x1="95" y1="930" x2="38" y2="873" marker-end="url(#tipLight)"/>
      <line x1="262" y1="930" x2="322" y2="870" marker-end="url(#tipLight)"/>
      <line x1="447" y1="930" x2="390" y2="873" marker-end="url(#tipLight)"/>
      <line x1="614" y1="930" x2="674" y2="870" marker-end="url(#tipLight)"/>
      <line x1="800" y1="930" x2="742" y2="873" marker-end="url(#tipLight)"/>
      <line x1="967" y1="930" x2="1027" y2="870" marker-end="url(#tipLight)"/>
    </g>

    <!-- service icons -->
    <g fill="none" stroke="#fbdd14" stroke-width="6" stroke-linejoin="round" stroke-linecap="round">
      <path d="M160,1000 L200,958 Q212,950 210,958 L205,998 L168,1016 Z"/>
      <circle cx="188" cy="985" r="7"/>
      <path d="M160,1000 L142,1000 L154,984 L172,982"/>
      <path d="M190,1008 L188,1026 L174,1014"/>
      <circle cx="146" cy="1020" r="6"/>
      <path d="M496,975 L530,975 L558,958 L558,1012 L530,996 L496,996 Z"/>
      <path d="M510,996 L514,1024 L522,1024 L520,996"/>
      <path d="M558,975 Q570,985 558,995"/>
    </g>
    <path d="M842,972 L862,972 L886,952 L886,1030 L862,1010 L842,1010 Z" fill="#fbdd14"/>
    <path d="M900,974 Q912,991 900,1008 M912,962 Q932,991 912,1020" fill="none" stroke="#fbdd14" stroke-width="7" stroke-linecap="round"/>
  </svg>

  <div class="brand">PageLantern</div>

  <p class="value value--left">We are fast &amp; nimble. We are creative and energetic.</p>
  <p class="value value--mid">We are dedicated and experienced. Disruption is crucial.</p>
  <p class="value value--right">Flawless execution is paramount.</p>

  <p class="intro intro--one"><strong>A book</strong> is a powerful weapon, one that establishes direction and provides a plan for growth. It represents the most meaningful narrative of your brand, making way for previously unreachable opportunities. Books are the tip of the thought leadership arrow.</p>
  <p class="intro intro--two"><strong>Writing</strong> a book is a challenging endeavor, therefore knowing where and how to direct your energy and resources to create a successful book launch is imperative. That’s why we’re here. We understand the art and science of the publishing world and most important - how to make your book a success.</p>

  <section class="service service--launch">
    <h2>Book Launch</h2>
    <p>So you wrote a great book. Now what? How do you get it into the hands and minds of the right people, the people who will connect with your idea, rally behind it, and catapult it to new heights?</p>
  </section>
  <section class="service service--airport">
    <h2>Airport<br>Advertising</h2>
    <p>Airport bookstores are the last remaining bookstores to capture the attention of influencers and decision makers. Imagine the impression made when a potential client</p>
  </section>
  <section class="service service--speaker">
    <h2>Speaker<br>Platform</h2>
    <p>Airport bookstores are the last remaining bookstores to capture the attention of influencers and decision makers. Imagine the impression made when a potential client</p>
  </section>

  <footer class="contact">
    <span style="left:20px">
      <svg width="14" height="18" viewBox="0 0 14 18"><path d="M7,0 C3,0 0,3 0,7 C0,12 7,18 7,18 C7,18 14,12 14,7 C14,3 11,0 7,0 Z" fill="#fbdd14"/><circle cx="7" cy="7" r="2.6" fill="#363638"/></svg>
      27 Harbor Lane Portland ME 04101
    </span>
    <span style="left:274px">
      <svg width="18" height="14" viewBox="0 0 18 14"><path d="M1,5 Q9,-1 17,5 L14,7 L12,4 L6,4 L4,7 Z M4,8 L14,8 L16,14 L2,14 Z" fill="#fbdd14"/></svg>
      +1 (555) 014-2736
    </span>
    <span style="left:438px">
      <svg width="18" height="13" viewBox="0 0 18 13"><rect x="1" y="1" width="16" height="11" fill="none" stroke="#fbdd14" stroke-width="1.6"/><path d="M1,1 L9,8 L17,1" fill="none" stroke="#fbdd14" stroke-width="1.6"/></svg>
      hello@pagelantern.com
    </span>
    <span style="left:657px">
      <svg width="18" height="18" viewBox="0 0 18 18" fill="none" stroke="#fbdd14" stroke-width="1.5"><circle cx="9" cy="9" r="8"/><ellipse cx="9" cy="9" rx="3.5" ry="8"/><line x1="1" y1="9" x2="17" y2="9"/><line x1="2.5" y1="5" x2="15.5" y2="5"/><line x1="2.5" y1="13" x2="15.5" y2="13"/></svg>
      www.pagelantern.com
    </span>
  </footer>
</main>
</body>
</html>
```